Software engineering company needs business card

I need a cool business card. Company: Belan Systems Brindlewood Ave 41 58207 Sincity Name: Gerald Vanholt CEO / Managing Director & Owner

```html
<!DOCTYPE html>
<html lang="de">
<head>
<meta charset="utf-8">
<title>Belan Systems – Visitenkarte</title>
<link rel="stylesheet" href="https://fonts.googleapis.com/css2?family=Open+Sans:wght@400;600;700&display=swap">
<style>
  :root {
    --page: #e9e6e1;
    --card-dark: #2f2d2b;
    --card-light: #ffffff;
    --ink: #2b2b2b;
    --green: #6bb33a;
    --green-dark: #4f8f25;
    --grey: #8a8a8a;
  }
  html, body {
    margin: 0;
    width: 1200px;
    height: 801px;
    overflow: hidden;
    background: var(--page);
    font-family: "Open Sans", sans-serif;
  }
  .stage {
    position: relative;
    width: 1200px;
    height: 801px;
  }
  .card {
    position: absolute;
    top: 238px;
    width: 500px;
    height: 324px;
    box-sizing: border-box;
    box-shadow: 0 10px 24px rgba(0,0,0,0.18);
  }
  .card--back {
    left: 70px;
    background: var(--card-dark);
    display: flex;
    align-items: center;
    justify-content: center;
  }
  .card--front {
    left: 630px;
    background: var(--card-light);
  }
  .brand {
    display: flex;
    align-items: center;
    gap: 12px;
    font-weight: 600;
    letter-spacing: 0.03em;
    white-space: nowrap;
  }
  .brand__mark {
    flex: none;
    width: 16px;
    height: 16px;
    background: var(--green);
  }
  .card--back .brand__name {
    color: var(--green);
    font-size: 38px;
  }
  .card--front .brand {
    position: absolute;
    left: 30px;
    top: 138px;
  }
  .card--front .brand__name {
    color: var(--grey);
    font-size: 22px;
  }
  .contact {
    position: absolute;
    left: 262px;
    top: 96px;
    color: var(--ink);
  }
  .contact__name {
    margin: 0;
    font-size: 22px;
    font-weight: 400;
    line-height: 1.1;
  }
  .contact__surname { font-weight: 700; }
  .contact__role {
    margin: 4px 0 16px;
    font-size: 13px;
    color: var(--green-dark);
  }
  .contact__list {
    list-style: none;
    margin: 0;
    padding: 0;
    font-size: 13px;
    line-height: 1.35;
  }
  .contact__item {
    display: flex;
    gap: 8px;
    margin-bottom: 6px;
  }
  .contact__icon {
    flex: none;
    width: 12px;
    height: 12px;
    margin-top: 2px;
    fill: var(--green);
  }
</style>
</head>
<body>
<main class="stage">
  <section class="card card--back" aria-label="Kartenrückseite">
    <div class="brand">
      <span class="brand__mark"></span>
      <span class="brand__name">Belan Systems</span>
    </div>
  </section>

  <section class="card card--front" aria-label="Kartenvorderseite">
    <div class="brand">
      <span class="brand__mark"></span>
      <span class="brand__name">Belan Systems</span>
    </div>
    <div class="contact">
      <h1 class="contact__name">Gerald <span class="contact__surname">Vanholt</span></h1>
      <p class="contact__role">CEO / Geschäftsführer &amp; Inhaber</p>
      <ul class="contact__list">
        <li class="contact__item">
          <svg class="contact__icon" viewBox="0 0 12 12"><path d="M6 0a4 4 0 0 0-4 4c0 3 4 8 4 8s4-5 4-8a4 4 0 0 0-4-4zm0 5.5A1.5 1.5 0 1 1 6 2.5a1.5 1.5 0 0 1 0 3z"/></svg>
          <span>Brindlewood Ave 41<br>58207 Sincity</span>
        </li>
        <li class="contact__item">
          <svg class="contact__icon" viewBox="0 0 12 12"><path d="M1 3c0-1 1-2 5-2s5 1 5 2v1H8V3H4v1H1zM2 5h8l1 6H1z"/></svg>
          <span>000 000 0000</span>
        </li>
        <li class="contact__item">
          <svg class="contact__icon" viewBox="0 0 12 12"><path d="M0 2h12v8H0zM1 3l5 4 5-4v-0.2H1z"/></svg>
          <span>youremail@xyz.com</span>
        </li>
      </ul>
    </div>
  </section>
</main>
</body>
</html>
```